Beautiful, sharp, website design for family-run property development company.

We are property developers in Kent (south east of London) who want to see the local town change. We are the only local property developer that is a family run business, focussing primarily on converting old, dilapidated Victorian buildings into beautiful residential spaces. Unlike other national developers, we work to regenerate buildings to create new employment opportunities, housing, and revive the town Centre .

Target Market(s)

1. Investors and Joint Venture partners - people with money to invest in property
2. Buyers of property - 25 to 40 year old, young professionals.
3. Commercial funders (people lending money to our projects
4. Professional team: Architects, builders, Estate agent who want to work with us

Industry/Entity Type

Real Estate Development

Coding

Number of Pages Required

Font styles to use
Other font styles liked:
• Please follow the brief of stylish, elegant, modern

Colors

Designer to choose colors to be used in the design.

Requirements
Must have
• Please use these websites as a reference of what we are looking to achieve.
• http://brellmoorhomes.com/#page5
• https://fernwick.co.uk/
• http://ambertide.co.uk/
• http://www.theharroweyestates.co.uk/about-harrowey
• Clean, simple, elegant, minimal design.
• Images of interiors of houses that have been converted from old buildings
• Images of farm buildings e.g. barns that have been converted to new homes or offices. Images of properties that may have been an old factory or old commercial property that is now a trendy apartment.
• Please use images of properties and interiors that are from the South East of England (including Kent, Surrey, Sussex, Hampshire, Dorset). There is a distinct style of housing in this part of England.
Nice to have
• Colours consistent with our brand colour palette (attached)

```html
<!DOCTYPE html>
<html lang="en">
<head>
<meta charset="utf-8">
<title>Ashcombe Lane Property – Website Design</title>
<link href="https://fonts.googleapis.com/css2?family=Montserrat:wght@400;500;600;700;800&family=Old+Standard+TT:wght@400;700&family=Playfair+Display:wght@400;700;900&display=swap" rel="stylesheet">
<style>
:root{
  --ink:#1f2725;
  --dark:#222a28;
  --deep:#1a2120;
  --teal:#7a9c93;
  --teal-dark:#5f8077;
  --paper:#ffffff;
  --mist:#efefef;
  --muted:#6f7775;
  --hero-a:#3b4346;
  --hero-b:#1e2426;
}
*{box-sizing:border-box;margin:0;padding:0}
html,body{width:1200px;height:2787px;overflow:hidden;background:var(--paper)}
body{font-family:'Montserrat',sans-serif;color:var(--ink)}
.stage{position:relative;width:1200px;height:2787px;overflow:hidden;background:var(--paper)}
.abs{position:absolute}
.top-band{left:0;top:0;width:1200px;height:650px;background:linear-gradient(160deg,#2d3836,#1c2422);clip-path:polygon(0 0,100% 0,100% 560px,0 648px)}
.brand-mark{left:0;width:1200px;text-align:center;color:#fff;font-family:'Montserrat',sans-serif;font-weight:500;letter-spacing:1px}
.brand-mark .name{font-size:24px}
.serif{font-family:'Old Standard TT',serif}
.display{font-family:'Playfair Display',serif}
.eyebrow{font-size:8px;letter-spacing:2px;color:var(--teal);text-transform:uppercase}
.title{font-family:'Old Standard TT',serif;color:var(--ink)}
.body-s{font-size:5.5px;line-height:1.6;color:var(--muted)}
.photo{background:linear-gradient(160deg,#8a949a,#3e474b)}
.hero{background:linear-gradient(180deg,var(--hero-a) 0%,#2a3134 55%,var(--hero-b) 100%);color:#fff;text-align:center;overflow:hidden}
.hero .kicker{font-weight:600}
.hero .headline{font-family:'Playfair Display',serif;font-weight:900;letter-spacing:1px;white-space:nowrap}
.btn{display:inline-block;background:var(--teal);color:#fff;font-weight:600;letter-spacing:.5px;white-space:nowrap}
.arrow{color:#fff;font-weight:300}
.site-header{background:#fff}
.logo-text{color:var(--teal);font-family:'Montserrat',sans-serif;font-weight:500;white-space:nowrap}
.nav{display:flex;color:var(--teal-dark);letter-spacing:1px;white-space:nowrap}
.contact-row{color:var(--ink);display:flex;gap:8px;white-space:nowrap}
.dark{background:var(--dark);color:#fff}
.mist{background:var(--mist)}
.card{background:#fff;text-align:center}
.date{background:#fff;color:var(--ink);text-align:center;font-family:'Old Standard TT',serif;line-height:1}
.date b{display:block;background:var(--ink);color:#fff;font-family:'Montserrat',sans-serif;font-weight:700}
.rule{background:var(--teal)}
.foot-list{list-style:none;color:#dfe5e3}
.dot{border-radius:50%;background:#cfd6d4}
.thanks{left:0;width:1200px;text-align:center;font-family:'Montserrat',sans-serif;font-weight:700;font-size:118px;letter-spacing:2px;color:var(--ink)}
</style>
</head>
<body>
<div class="stage">

  <div class="abs top-band"></div>
  <div class="abs brand-mark" style="top:78px">
    <div class="name">ASHCOMBE LANE</div>
    <div style="font-size:9px;letter-spacing:4px;margin-top:2px">PROPERTY</div>
  </div>

  <!-- desktop screen, hero view -->
  <div class="abs" style="left:251px;top:152px;width:699px;height:403px;background:#fff;overflow:hidden">
    <div class="abs site-header" style="left:0;top:0;width:699px;height:36px">
      <div class="abs logo-text" style="left:52px;top:20px;font-size:7px">ASHCOMBE LANE</div>
      <div class="abs contact-row" style="right:50px;top:4px;font-size:7px">
        <span>&#9742; +44 1622 555 018</span><span>&#9993; hello@ashcombelane.co.uk</span>
      </div>
      <div class="abs nav" style="left:316px;top:21px;font-size:7px;gap:52px">
        <span>HOME</span><span style="color:var(--ink)">PROJECTS</span><span style="color:var(--ink)">ABOUT</span><span style="color:var(--ink)">BLOG</span><span style="color:var(--ink)">CONTACT</span>
      </div>
    </div>
    <div class="abs hero" role="img" aria-label="Dark grey two-storey family house with gabled roofs behind a black railing fence, trees on either side" style="left:0;top:36px;width:699px;height:285px">
      <div class="abs kicker" style="left:0;width:699px;top:86px;font-size:19px">Redesigned</div>
      <div class="abs headline" style="left:0;width:699px;top:104px;font-size:50px">Your Perfect Home</div>
      <div class="abs" style="left:160px;width:379px;top:166px;font-size:9px;line-height:1.6">It is a long established fact that a reader will be distracted by the readable content of a page when looking at its layout.</div>
      <div class="abs btn" style="left:302px;top:207px;width:93px;height:26px;line-height:26px;font-size:11px">CONTACT US</div>
      <div class="abs arrow" style="left:58px;top:140px;font-size:22px">&#8249;</div>
      <div class="abs arrow" style="left:628px;top:140px;font-size:22px">&#8250;</div>
    </div>
    <div class="abs photo" role="img" aria-label="Timber frame of a house under construction against blue sky" style="left:342px;top:375px;width:357px;height:28px;background:linear-gradient(90deg,#cfe0ee,#9bbbd6)"></div>
  </div>

  <!-- mobile screen, hero view -->
  <div class="abs" style="left:918px;top:300px;width:175px;height:290px;background:#fff;overflow:hidden">
    <div class="abs logo-text" style="left:8px;top:20px;font-size:5.5px">ASHCOMBE LANE</div>
    <div class="abs" style="right:6px;top:10px;width:15px">
      <div style="height:2px;background:var(--teal-dark);margin-bottom:3px"></div>
      <div style="height:2px;background:var(--teal-dark);margin-bottom:3px"></div>
      <div style="height:2px;background:var(--teal-dark)"></div>
    </div>
    <div class="abs hero" role="img" aria-label="Dark grey family house with gabled roofs" style="left:0;top:35px;width:175px;height:75px"></div>
    <div class="abs" style="left:0;width:175px;top:126px;text-align:center">
      <div style="font-size:9px;font-weight:600">Redesigned</div>
      <div class="display" style="font-size:13px;font-weight:700;margin-top:2px">Your Perfect Home</div>
      <div style="font-size:7px;line-height:1.5;color:var(--ink);padding:3px 8px">It is a long established fact that a reader will be distracted by the readable content of a page when looking at its layout.</div>
      <div class="btn" style="font-size:6.5px;padding:4px 6px;margin-top:2px">CONTACT US</div>
    </div>
    <div class="abs photo" role="img" aria-label="House frame under construction with green sheathing" style="left:10px;top:235px;width:155px;height:55px;background:linear-gradient(180deg,#bcd5ea,#6f8f6a)"></div>
  </div>

  <div class="abs display" style="left:280px;top:710px;font-size:70px;color:var(--ink);text-shadow:2px 3px 4px rgba(0,0,0,.3)">Desktop</div>

  <!-- ===== desktop page ===== -->
  <div class="abs site-header" style="left:136px;top:822px;width:534px;height:31px">
    <div class="abs logo-text" style="left:42px;top:20px;font-size:5.5px">ASHCOMBE LANE</div>
    <div class="abs contact-row" style="right:42px;top:4px;font-size:5px"><span>&#9742; +44 1622 555 018</span><span>&#9993; hello@ashcombelane.co.uk</span></div>
    <div class="abs nav" style="left:242px;top:19px;font-size:5px;gap:36px"><span>HOME</span><span style="color:var(--ink)">PROJECTS</span><span style="color:var(--ink)">ABOUT</span><span style="color:var(--ink)">BLOG</span><span style="color:var(--ink)">CONTACT</span></div>
  </div>
  <div class="abs hero" role="img" aria-label="Dark grey two-storey family house behind a black railing fence" style="left:136px;top:853px;width:534px;height:233px">
    <div class="abs kicker" style="left:0;width:534px;top:68px;font-size:14px">Redesigned</div>
    <div class="abs headline" style="left:0;width:534px;top:84px;font-size:38px">Your Perfect Home</div>
    <div class="abs" style="left:120px;width:294px;top:135px;font-size:7px;line-height:1.6">It is a long established fact that a reader will be distracted by the readable content of a page when looking at its layout.</div>
    <div class="abs btn" style="left:232px;top:168px;width:70px;height:19px;line-height:19px;font-size:8px">CONTACT US</div>
    <div class="abs arrow" style="left:46px;top:100px;font-size:18px">&#8249;</div>
    <div class="abs arrow" style="left:480px;top:100px;font-size:18px">&#8250;</div>
  </div>

  <!-- about -->
  <div class="abs eyebrow" style="left:178px;top:1176px;font-size:7px">ABOUT US</div>
  <div class="abs title" style="left:178px;top:1187px;font-size:21px;line-height:22px;width:200px">Ashcombe Lane<br>Property</div>
  <div class="abs body-s" style="left:178px;top:1241px;width:202px">It is a long established fact that a reader will be distracted by the readable content of a page when looking at its layout. The point of using Lorem Ipsum is that it has a more-or-less normal distribution of letters, as opposed to using 'Content here, content here', making it look like readable English. Many desktop publishing packages and web ...</div>
  <div class="abs" style="left:178px;top:1295px;font-size:7px;font-weight:700">READ MORE &rsaquo;</div>
  <div class="abs photo" role="img" aria-label="Timber-framed building with green sheathing under construction and a yellow telehandler in front" style="left:397px;top:1131px;width:232px;height:218px;background:linear-gradient(180deg,#cfe0ef 0%,#b98f64 40%,#3f7a55 70%,#8a8a84 100%)"></div>

  <!-- gallery -->
  <div class="abs mist" style="left:136px;top:1393px;width:534px;height:314px"></div>
  <div class="abs eyebrow" style="left:136px;width:534px;text-align:center;top:1436px;font-size:7px">OUR GALLERY</div>
  <div class="abs title" style="left:136px;width:534px;text-align:center;top:1447px;font-size:22px">Other Projects</div>
  <div class="abs rule" style="left:394px;top:1476px;width:18px;height:1px"></div>
  <div class="abs" style="left:186px;top:1547px;font-size:22px;color:var(--ink)">&#8249;</div>
  <div class="abs" style="left:608px;top:1547px;font-size:22px;color:var(--muted)">&#8250;</div>
  <div class="abs photo" role="img" aria-label="Modern apartment tower with dark glass and terracotta balconies" style="left:206px;top:1497px;width:187px;height:117px;background:linear-gradient(90deg,#3b4148 0%,#5e6670 55%,#b56a4a 80%,#d9d6d0 100%)"></div>
  <div class="abs photo" role="img" aria-label="Large cream family house with grey roof and green lawn under blue sky" style="left:411px;top:1497px;width:187px;height:117px;background:linear-gradient(180deg,#5c9be0 0%,#c9c1b3 55%,#5f9a3c 100%)"></div>
  <div class="abs title" style="left:206px;width:187px;text-align:center;top:1621px;font-size:11px">There are many variations</div>
  <div class="abs body-s" style="left:212px;width:175px;text-align:center;top:1637px">Lorem Ipsum is simply dummy text of the printing and typesetting industry. Lorem Ipsum has been the industry's standard dummy text ever since the 1500s</div>
  <div class="abs title" style="left:411px;width:187px;text-align:center;top:1621px;font-size:11px">There are many variations</div>
  <div class="abs body-s" style="left:417px;width:175px;text-align:center;top:1637px">Lorem Ipsum is simply dummy text of the printing and typesetting industry. Lorem Ipsum has been the industry's standard dummy text ever since the 1500s</div>

  <!-- blog -->
  <div class="abs dark" style="left:136px;top:1707px;width:534px;height:323px"></div>
  <div class="abs" style="left:136px;width:534px;text-align:center;top:1747px;font-size:7px;letter-spacing:2px;color:#e3e8e6">LATEST NEWS</div>
  <div class="abs title" style="left:136px;width:534px;text-align:center;top:1757px;font-size:22px;color:#fff">From Our Blog</div>
  <div class="abs" style="left:394px;top:1787px;width:18px;height:1px;background:#fff"></div>

  <div class="abs photo" role="img" aria-label="White modern villa with balconies against a pale sky" style="left:178px;top:1812px;width:141px;height:105px;background:linear-gradient(180deg,#c9d6e2,#e7e3da 60%,#9aa08d)"></div>
  <div class="abs photo" role="img" aria-label="Blue clapboard house with white trim and autumn trees" style="left:332px;top:1812px;width:141px;height:105px;background:linear-gradient(180deg,#b9c6d4,#3e5a86 50%,#6b5a3c)"></div>
  <div class="abs photo" role="img" aria-label="Glass office building facade reflecting blue sky" style="left:487px;top:1812px;width:141px;height:105px;background:linear-gradient(135deg,#e7f1f4,#7fb4c0 55%,#d4e2e4)"></div>

  <div class="abs date" style="left:183px;top:1819px;width:18px;font-size:8px;padding-top:1px">12<b style="font-size:4px;margin-top:1px">JAN</b></div>
  <div class="abs date" style="left:338px;top:1819px;width:18px;font-size:8px;padding-top:1px">12<b style="font-size:4px;margin-top:1px">JAN</b></div>
  <div class="abs date" style="left:493px;top:1819px;width:18px;font-size:8px;padding-top:1px">12<b style="font-size:4px;margin-top:1px">JAN</b></div>

  <div class="abs card" style="left:186px;top:1910px;width:125px;height:65px;padding-top:9px">
    <div class="title" style="font-size:9px">Contrary to popular</div>
    <div class="body-s" style="padding:2px 8px 0">It is a long established fact that a reader will be distracted by the readable...</div>
    <div style="font-size:4.5px;color:var(--teal);margin-top:2px">READ MORE</div>
  </div>
  <div class="abs card" style="left:340px;top:1910px;width:125px;height:65px;padding-top:9px">
    <div class="title" style="font-size:9px">Contrary to popular</div>
    <div class="body-s" style="padding:2px 8px 0">It is a long established fact that a reader will be distracted by the readable...</div>
    <div style="font-size:4.5px;color:var(--teal);margin-top:2px">READ MORE</div>
  </div>
  <div class="abs card" style="left:495px;top:1910px;width:125px;height:65px;padding-top:9px">
    <div class="title" style="font-size:9px">Contrary to popular</div>
    <div class="body-s" style="padding:2px 8px 0">It is a long established fact that a reader will be distracted by the readable...</div>
    <div style="font-size:4.5px;color:var(--teal);margin-top:2px">READ MORE</div>
  </div>
  <div class="abs" style="left:389px;top:1994px;width:28px;height:1px;border-top:1px dashed #cfd6d4"></div>

  <!-- like our work -->
  <div class="abs" style="left:136px;top:2154px;width:534px;height:75px;background:#f7f7f7"></div>
  <div class="abs title" style="left:136px;width:534px;text-align:center;top:2070px;font-size:22px">Like Our Work</div>
  <div class="abs rule" style="left:394px;top:2099px;width:18px;height:1px"></div>
  <div class="abs body-s" style="left:205px;width:396px;text-align:center;top:2112px">It is a long established fact that a reader will be distracted by the readable content of a page when looking at its layout. The point of using Lorem Ipsum is that it has a more-or-less normal distribution of letters, as opposed to using 'Content here, content here', making it look like readable English. Many desktop publishing packages and web page editors now use Lorem Ipsum as their default model text, and a search for 'lorem ipsum' will uncover many web sites still in their infancy.</div>
  <div class="abs btn" style="left:371px;top:2166px;width:64px;height:15px;line-height:15px;font-size:5.5px;text-align:center">CONTACT US &rsaquo;</div>

  <!-- desktop footer -->
  <div class="abs dark" style="left:136px;top:2229px;width:534px;height:146px"></div>
  <div class="abs" style="left:136px;top:2375px;width:534px;height:13px;background:var(--deep);color:#cfd6d4;font-size:5px;text-align:center;line-height:13px"><span style="color:var(--teal)">&copy; Ashcombe Lane Property</span> 2020. All Rights Reserved.</div>
  <div class="abs" style="left:178px;top:2269px;font-size:7px;color:#fff">ASHCOMBE LANE</div>
  <div class="abs" style="left:178px;top:2290px;width:120px;font-size:5px;line-height:1.6;color:#dfe5e3">Lorem Ipsum is simply dummy text of the printing and typesetting industry.</div>
  <div class="abs" style="left:180px;top:2316px;display:flex;gap:5px"><div class="dot" style="width:9px;height:9px"></div><div class="dot" style="width:9px;height:9px"></div><div class="dot" style="width:9px;height:9px"></div></div>
  <div class="abs serif" style="left:331px;top:2260px;font-size:7px">Quick Links</div>
  <div class="abs" style="left:331px;top:2270px;width:14px;height:1px;background:#fff"></div>
  <ul class="abs foot-list" style="left:331px;top:2277px;font-size:5px;line-height:14.5px"><li>&rsaquo; Home</li><li>&rsaquo; Projects</li><li>&rsaquo; About</li><li>&rsaquo; Blog</li><li>&rsaquo; Contact</li></ul>
  <div class="abs serif" style="left:422px;top:2260px;font-size:7px">Support</div>
  <div class="abs" style="left:422px;top:2270px;width:14px;height:1px;background:#fff"></div>
  <ul class="abs foot-list" style="left:422px;top:2277px;font-size:5px;line-height:14.5px"><li>&rsaquo; Forum</li><li>&rsaquo; Statistics</li><li>&rsaquo; Terms and Condition</li><li>&rsaquo; Get Support</li><li>&rsaquo; Frequently Ask Question</li></ul>
  <div class="abs serif" style="left:533px;top:2260px;font-size:7px">Contact Us</div>
  <div class="abs" style="left:533px;top:2270px;width:14px;height:1px;background:#fff"></div>
  <ul class="abs foot-list" style="left:533px;top:2277px;font-size:5px;line-height:8px;width:110px"><li>&#9679; 14 Mill Street, Maidstone<br>&nbsp;&nbsp;Kent ME15 6XH</li><li style="margin-top:6px">&#9742; +44 1622 555 018</li><li style="margin-top:6px">&#9993; hello@ashcombelane.co.uk</li></ul>

  <!-- ===== mobile page ===== -->
  <div class="abs" style="left:918px;top:700px;width:176px;text-align:center">
    <div class="eyebrow" style="font-size:7px">ABOUT US</div>
    <div class="title" style="font-size:12px;line-height:14px;margin-top:2px">Ashcombe Lane<br>Property</div>
    <div class="body-s" style="padding:6px 12px 0">It is a long established fact that a reader will be distracted by the readable content of a page when looking at its layout. The point of using Lorem Ipsum is that it has a more-or-less normal distribution of letters, as opposed to using 'Content here, content here', making it look like readable English. Many desktop publishing packages and web ...</div>
    <div style="font-size:7px;font-weight:700;margin-top:6px">READ MORE &raquo;</div>
  </div>

  <div class="abs mist" style="left:918px;top:873px;width:176px;height:214px"></div>
  <div class="abs" style="left:918px;top:894px;width:176px;text-align:center">
    <div class="eyebrow" style="font-size:7px">OUR GALLERY</div>
    <div class="title" style="font-size:12px;margin-top:1px">Other Projects</div>
  </div>
  <div class="abs" style="left:930px;top:955px;font-size:14px">&#8249;</div>
  <div class="abs" style="left:1072px;top:955px;font-size:14px">&#8250;</div>
  <div class="abs photo" role="img" aria-label="Modern apartment tower with terracotta balconies" style="left:943px;top:929px;width:126px;height:78px;background:linear-gradient(90deg,#3b4148,#5e6670 55%,#b56a4a 80%,#d9d6d0)"></div>
  <div class="abs" style="left:918px;top:1011px;width:176px;text-align:center">
    <div class="title" style="font-size:9px">There are many variations</div>
    <div class="body-s" style="padding:2px 16px 0">Lorem Ipsum is simply dummy text of the printing and typesetting industry. Lorem Ipsum has been the industry's standard dummy text ever since the 1500s</div>
  </div>

  <div class="abs dark" style="left:918px;top:1087px;width:176px;height:238px"></div>
  <div class="abs" style="left:918px;top:1109px;width:176px;text-align:center">
    <div style="font-size:7px;letter-spacing:2px;color:#e3e8e6">LATEST NEWS</div>
    <div class="title" style="font-size:12px;color:#fff;margin-top:1px">From Our Blog</div>
  </div>
  <div class="abs photo" role="img" aria-label="White modern villa with balconies" style="left:947px;top:1148px;width:118px;height:112px;background:linear-gradient(180deg,#c9d6e2,#e7e3da 60%,#9aa08d)"></div>
  <div class="abs date" style="left:953px;top:1156px;width:15px;font-size:7px;padding-top:1px">12<b style="font-size:4px;margin-top:1px">JAN</b></div>
  <div class="abs card" style="left:953px;top:1233px;width:106px;height:52px;padding-top:8px">
    <div class="title" style="font-size:8px">Contrary to popular</div>
    <div class="body-s" style="padding:2px 8px 0;font-size:4.5px">It is a long established fact that a reader will be distracted by the readable...</div>
    <div style="font-size:4px;color:var(--teal);margin-top:2px">READ MORE</div>
  </div>
  <div class="abs" style="left:991px;top:1301px;width:30px;height:1px;border-top:1px dashed #cfd6d4"></div>

  <div class="abs" style="left:918px;top:1330px;width:176px;height:183px;background:#f7f7f7"></div>
  <div class="abs" style="left:918px;top:1345px;width:176px;text-align:center">
    <div class="title" style="font-size:12px">Like Our Work</div>
    <div class="body-s" style="padding:7px 12px 0">It is a long established fact that a reader will be distracted by the readable content of a page when looking at its layout. The point of using Lorem Ipsum is that it has a more-or-less normal distribution of letters, as opposed to using 'Content here, content here', making it look like readable English. Many desktop publishing packages and web page editors now use Lorem Ipsum as their default model text, and a search for 'lorem ipsum' will uncover many web sites still in their infancy.</div>
    <div class="btn" style="font-size:6px;padding:4px 7px;margin-top:7px">CONTACT US &raquo;</div>
  </div>

  <div class="abs dark" style="left:918px;top:1513px;width:176px;height:512px"></div>
  <div class="abs" style="left:928px;top:1562px;font-size:7px;color:#fff">ASHCOMBE LANE</div>
  <div class="abs" style="left:928px;top:1585px;width:140px;font-size:5.5px;line-height:1.6;color:#dfe5e3">Lorem Ipsum is simply dummy text of the printing and typesetting industry.</div>
  <div class="abs serif" style="left:928px;top:1616px;font-size:9px;color:#fff">Quick Links</div>
  <div class="abs" style="left:928px;top:1629px;width:18px;height:1px;background:#fff"></div>
  <ul class="abs foot-list" style="left:928px;top:1641px;font-size:6px;line-height:19px"><li>&rsaquo; Home</li><li>&rsaquo; Projects</li><li>&rsaquo; About</li><li>&rsaquo; Blog</li><li>&rsaquo; Contact</li></ul>
  <div class="abs serif" style="left:928px;top:1746px;font-size:9px;color:#fff">Support</div>
  <div class="abs" style="left:928px;top:1759px;width:18px;height:1px;background:#fff"></div>
  <ul class="abs foot-list" style="left:928px;top:1770px;font-size:6px;line-height:19px"><li>&rsaquo; Forum</li><li>&rsaquo; Statistics</li><li>&rsaquo; Terms and Condition</li><li>&rsaquo; Get Support</li><li>&rsaquo; Frequently Ask Question</li></ul>
  <div class="abs serif" style="left:928px;top:1875px;font-size:9px;color:#fff">Contact Us</div>
  <div class="abs" style="left:928px;top:1888px;width:18px;height:1px;background:#fff"></div>
  <ul class="abs foot-list" style="left:928px;top:1900px;font-size:6px;line-height:10px;width:150px"><li>&#9679; 14 Mill Street, Maidstone<br>&nbsp;&nbsp;Kent ME15 6XH</li><li style="margin-top:8px">&#9742; +44 1622 555 018</li><li style="margin-top:8px">&#9993; hello@ashcombelane.co.uk</li></ul>
  <div class="abs" style="left:968px;top:1978px;display:flex;gap:9px"><div class="dot" style="width:16px;height:16px"></div><div class="dot" style="width:16px;height:16px"></div><div class="dot" style="width:16px;height:16px"></div></div>
  <div class="abs" style="left:918px;top:2025px;width:176px;height:41px;background:var(--deep);color:#cfd6d4;font-size:5.5px;text-align:center;padding-top:13px;line-height:1.6"><span style="color:var(--teal)">&copy; Ashcombe Lane Property</span> 2020.<br>All Rights Reserved.</div>

  <!-- closing brand name -->
  <div class="abs" style="left:700px;top:2380px;width:500px;text-align:center;font-family:'Montserrat',sans-serif;font-weight:600;color:var(--teal);line-height:1">
    <div style="font-size:50px;letter-spacing:1px;white-space:nowrap">ASHCOMBE LANE</div>
    <div style="font-size:24px;letter-spacing:9px;margin-top:10px">PROPERTY</div>
  </div>

  <div class="abs thanks" style="top:2610px">THANK YOU</div>
</div>
</body>
</html>
```